Design my dad a new business card because his current one sucks!

I need a business card designed for my fathers home maintenance business. His customers are individuals (single moms, old people etc.) as well as the occasional business. As such it needs to be accessible to both target audiences.

The front of the card should be dark grey on yellow with the logo and contain the following information:
- Warren Dobrinski
- 0487 362 914
- info@harbourlinehandyworks.com.au
- 0487 362 914

- ABN: 87 214 630 592
- 'Fully Insured'

The reverse should be yellow on dark grey and will have the web address:
- harbourlinehandyworks.com.au

And a few key services he offers:
GENERAL REPAIRS
PAINTING/TILING/
PAVING &CONCRETING
PRESSURE WASHING
ON-SITE WELDING
DECKING ADDITIONS & REPAIRS
FENCING
FULL BOND CLEANING

This will be first time the logo has been printed so you will need to come up with the best CMYK approximation of the RGB colours to make sure it is a close as possible.

```html
<!DOCTYPE html>
<html lang="en">
<head>
<meta charset="utf-8">
<title>Harbourline Handyworks – Business Card</title>
<link rel="stylesheet" href="https://fonts.googleapis.com/css2?family=Open+Sans:wght@400;600;700&display=swap">
<style>
  :root {
    --backdrop: #e4e4e4;
    --card-yellow: #e9c916;
    --card-grey: #4f4f51;
    --ink-grey: #454547;
    --ink-yellow: #e9c916;
    --edge-grey: #5a5a5a;
  }
  * { box-sizing: border-box; margin: 0; padding: 0; }
  html, body {
    width: 1200px;
    height: 730px;
    overflow: hidden;
    background: var(--backdrop);
    font-family: "Open Sans", Arial, sans-serif;
  }
  .card-set {
    position: absolute;
    top: 145px;
    left: 130px;
    display: flex;
    gap: 60px;
  }
  .card {
    width: 440px;
    height: 440px;
    position: relative;
    text-align: center;
  }
  .card--front {
    background: var(--card-yellow);
    color: var(--ink-grey);
    border: 3px solid var(--edge-grey);
  }
  .card--back {
    background: var(--card-grey);
    color: var(--ink-yellow);
    border: 3px solid var(--card-yellow);
  }

  /* Front */
  .brand {
    position: absolute;
    top: 38px;
    left: 0;
    right: 0;
    display: flex;
    align-items: center;
    justify-content: center;
    gap: 10px;
  }
  .brand__dot { width: 26px; height: 26px; }
  .brand__name {
    font-weight: 700;
    font-size: 27px;
    letter-spacing: -0.3px;
  }
  .holder-name {
    position: absolute;
    top: 110px;
    left: 0; right: 0;
    font-size: 27px;
    font-weight: 400;
  }
  .contact-list {
    position: absolute;
    top: 178px;
    left: 0; right: 0;
    list-style: none;
    font-size: 16px;
    line-height: 1.3;
  }
  .contact-list__email { font-weight: 700; }
  .insured {
    position: absolute;
    top: 288px;
    left: 0; right: 0;
    font-size: 25px;
  }
  .abn {
    position: absolute;
    left: 16px;
    bottom: 12px;
    font-size: 18px;
    text-align: left;
  }

  /* Back */
  .service-list {
    position: absolute;
    top: 48px;
    left: 0; right: 0;
    list-style: none;
    font-size: 17px;
    line-height: 1.55;
    text-transform: uppercase;
  }
  .web-address {
    position: absolute;
    bottom: 40px;
    left: 0; right: 0;
    font-size: 18px;
    font-weight: 700;
  }
</style>
</head>
<body>
  <main class="card-set">
    <section class="card card--front" aria-label="Card front">
      <div class="brand">
        <svg class="brand__dot" viewBox="0 0 26 26" aria-hidden="true">
          <circle cx="13" cy="13" r="12" fill="#454547"/>
        </svg>
        <span class="brand__name">Harbourline Handyworks</span>
      </div>
      <h1 class="holder-name">Warren Dobrinski</h1>
      <ul class="contact-list">
        <li>0487 362 914</li>
        <li class="contact-list__email">info@harbourlinehandyworks.com.au</li>
        <li>0487 362 914</li>
      </ul>
      <p class="insured">Fully Insured</p>
      <p class="abn">ABN: 87 214 630 592</p>
    </section>

    <section class="card card--back" aria-label="Card back">
      <ul class="service-list">
        <li>General Repairs</li>
        <li>Painting/Tiling/</li>
        <li>Paving &amp; Concreting</li>
        <li>Pressure Washing</li>
        <li>On-Site Welding</li>
        <li>Decking Additions &amp; Repairs</li>
        <li>Fencing</li>
        <li>Full Bond Cleaning</li>
      </ul>
      <p class="web-address">www.harbourlinehandyworks.com.au</p>
    </section>
  </main>
</body>
</html>
```